Gather the Marrow Book Cover

Looking for a cover for my book, Gather the Marrow. Part memoir, part self help - this book is one woman's journey breaking free of the patriarchy and stepping into her divine purpose. Think "boss ass bitch" in NYC transitions to Spiritual Goddess to the beaches of Costa Rica. We are playing on the archetypes of Wounded Masculine to Divine Feminine. Breaking the mold of being a good girl and owning her wild.

Target Market(s)

25-35 yr old female

Industry/Entity Type

Personal Development, Memoir

Other font styles liked:
• Pink #ff0099 Yellow #ffdf2b Teal #1fc4cd Gather - Brittany The - open sans Marrow - Bebas Neue

Colors
FFF300
FFF600
FEFA6F
FFFEC7
FFFEE8
E54698
E96AAD
F1A4CE
F9D9EA
FCEFF6

Requirements
Nice to have

```html
<!DOCTYPE html>
<html lang="en">
<head>
<meta charset="utf-8">
<title>Gather the Marrow — Book Cover</title>
<link rel="stylesheet" href="https://fonts.googleapis.com/css2?family=Bebas+Neue&family=Sacramento&family=Open+Sans:wght@700&display=swap">
<style>
  :root {
    --paper: #ffffff;
    --pink: #e54698;
    --pink-soft: #f1a4ce;
    --yellow: #fff300;
    --yellow-soft: #fefa6f;
    --plum: #2a0f24;
    --plum-mid: #6b2a55;
    --ink: #141014;
  }
  html, body {
    margin: 0;
    padding: 0;
    overflow: hidden;
    background: var(--paper);
  }
  .cover {
    position: relative;
    width: 826px;
    height: 1200px;
    overflow: hidden;
    background:
      radial-gradient(ellipse 420px 600px at 640px 520px, #fffdf3 0%, var(--paper) 70%);
  }
  .author-name {
    position: absolute;
    top: 34px;
    left: 0;
    width: 826px;
    margin: 0;
    text-align: center;
    font-family: "Bebas Neue", sans-serif;
    font-weight: 400;
    font-size: 70px;
    letter-spacing: 0.28em;
    text-indent: 0.28em;
    color: var(--pink);
    line-height: 1;
  }
  .portrait-art {
    position: absolute;
    left: 0;
    top: 150px;
    width: 760px;
    height: 1050px;
    border-radius: 48% 52% 0 0 / 32% 36% 0 0;
    background:
      radial-gradient(ellipse 180px 420px at 250px 460px, rgba(255, 246, 0, 0.75) 0%, rgba(255, 246, 0, 0) 70%),
      radial-gradient(ellipse 260px 300px at 240px 240px, rgba(233, 106, 173, 0.85) 0%, rgba(233, 106, 173, 0) 75%),
      linear-gradient(100deg, var(--plum) 0%, var(--plum-mid) 35%, #3a2b30 62%, #cfc9c4 88%, #f4f1ee 100%);
  }
  .title {
    position: absolute;
    left: 0;
    top: 0;
    width: 826px;
    height: 1200px;
    margin: 0;
    font-weight: 400;
  }
  .title-script {
    position: absolute;
    left: 385px;
    top: 790px;
    font-family: "Sacramento", cursive;
    font-size: 170px;
    line-height: 1;
    color: var(--pink);
    transform: rotate(-22deg);
    transform-origin: left bottom;
  }
  .title-joiner {
    position: absolute;
    left: 540px;
    top: 960px;
    font-family: "Open Sans", sans-serif;
    font-weight: 700;
    font-size: 40px;
    line-height: 1;
    color: var(--pink);
  }
  .title-main {
    position: absolute;
    left: 300px;
    top: 1005px;
    font-family: "Bebas Neue", sans-serif;
    font-size: 150px;
    line-height: 1;
    letter-spacing: 0.01em;
    color: var(--yellow);
    text-shadow: 4px 5px 8px rgba(20, 16, 20, 0.55);
  }
</style>
</head>
<body>
  <main class="cover">
    <p class="author-name">Author Name</p>

    <div class="portrait-art" role="img"
         aria-label="Profile silhouette of a woman with a glowing sacred-geometry figure, moons and circles overlaid on her head in pink and yellow light"></div>

    <h1 class="title">
      <span class="title-script">Gather</span>
      <span class="title-joiner">the</span>
      <span class="title-main">MARROW</span>
    </h1>
  </main>
</body>
</html>
```